Powerpoint master slides for business

Hello everyone,

I am looking for a new PowerPoint master slide that should be modern, slim and yet suitable for business.

I have uploaded a few pictures, which should serve as A. orientation for my presentation. A logo should be placed on the right-hand side of the cover sheet and all subsequent slides - please insert a placeholder here. Also attached are our company colors, which must be taken into account.

Basically, I would find 6 to 10 slides (cover sheet, classic slide, end, etc.) good.

PS: The slides are intended for general everyday work, ie the design should be subtle and easily adaptable to different situations, but still look chic, modern and classy.

```html
<!DOCTYPE html>
<html lang="en">
<head>
<meta charset="utf-8">
<title>Business Master Slides</title>
<link href="https://fonts.googleapis.com/css2?family=Montserrat:wght@300;400;500;600;700;800&display=swap" rel="stylesheet">
<style>
  :root{
    --backdrop:#d4d4d4;
    --paper:#ececec;
    --navy:#1c3a73;
    --deep-blue:#12344f;
    --gold:#e0ae21;
    --ink:#262626;
    --text:#3a3a3a;
    --muted:#6b6b6b;
    --grey-1:#8a8a8a;
    --grey-2:#6e6e6e;
    --grey-3:#555;
    --grey-4:#434343;
  }
  *{box-sizing:border-box;margin:0;padding:0}
  html,body{width:1200px;height:800px;overflow:hidden}
  body{background:var(--backdrop);font-family:'Montserrat',sans-serif;color:var(--text)}
  .deck{position:absolute;left:146px;top:11px;display:grid;grid-template-columns:441.6px 441.6px;grid-auto-rows:248.4px;gap:16px 24px}
  .frame{width:441.6px;height:248.4px;box-shadow:0 4px 12px rgba(0,0,0,.18);overflow:hidden}
  .slide{width:960px;height:540px;position:relative;background:var(--paper);overflow:hidden;transform:scale(.46);transform-origin:0 0}

  .footer-band{position:absolute;left:0;right:0;bottom:0;height:56px;background:var(--ink)}
  .footer-band .logo-mark{position:absolute;left:36px;top:6px;font-size:34px;font-weight:300;color:#e6e6e6;letter-spacing:1px}
  .footer-band .page-no{position:absolute;right:28px;top:20px;font-size:11px;color:#bdbdbd}

  .slide-header{position:absolute;left:40px;top:38px;display:flex;align-items:center;gap:12px}
  .slide-header .bar{width:6px;height:22px;background:var(--ink)}
  .slide-header h2{font-size:26px;font-weight:700;color:var(--navy);letter-spacing:1px}
  .header-rule{position:absolute;top:58px;height:2px;background:var(--ink)}
  .header-rule::after{content:"";position:absolute;right:-3px;top:-3px;width:8px;height:8px;background:var(--ink)}

  .photo{position:absolute;background:linear-gradient(180deg,#d3dce6 0%,#a5b5c6 40%,#66798e 75%,#4b5a6b 100%)}
  .hall-photo{background:radial-gradient(circle at 50% 35%,#c4cad0 0%,#8d949c 55%,#5f6872 100%)}

  .body-copy{font-size:14px;line-height:1.55;color:var(--text)}
  .item-title{font-size:20px;font-weight:500;color:var(--navy)}
  .item-copy{font-size:12px;line-height:1.5;color:var(--muted)}

  /* cover */
  .cover .photo{left:30px;top:40px;width:870px;height:300px}
  .cover .top-block{position:absolute;left:600px;top:18px;width:230px;height:56px;background:var(--ink)}
  .cover .logo-box{position:absolute;left:640px;top:270px;width:260px;height:120px;background:var(--ink);display:flex;align-items:center;justify-content:center}
  .cover .logo-box span{font-size:52px;font-weight:300;color:#eee}
  .cover .accent{position:absolute;left:0;top:400px;width:26px;height:100px;background:var(--gold)}
  .cover .title{position:absolute;left:64px;top:388px;color:var(--navy);font-weight:800;line-height:.95}
  .cover .title .big{font-size:78px;display:block}
  .cover .title .small{font-size:50px;display:block;margin-left:6px}

  /* text + photo */
  .intro .dark-panel{position:absolute;inset:0}
  .intro .body-copy{position:absolute;left:60px;top:110px;width:440px}
  .intro .icon-row{position:absolute;left:60px;display:flex;align-items:center;gap:22px}
  .intro .icon-row .divider{width:3px;height:44px;background:var(--gold)}
  .intro .icon-row p{width:380px;font-size:13px;line-height:1.5}

  /* grid */
  .grid{position:absolute;left:60px;top:110px;width:840px;height:300px;display:grid;grid-template-columns:repeat(4,1fr);grid-template-rows:1fr 1fr;border:4px solid var(--deep-blue)}
  .cell{position:relative;border:2px solid var(--deep-blue);display:flex;align-items:center;justify-content:center}
  .cell.gold{background:var(--gold)}
  .cell.plain{background:var(--paper);flex-direction:column;align-items:flex-start;padding:0 26px;gap:8px}
  .cell .item-copy{font-size:11px}

  /* circles */
  .feature{position:absolute;top:92px;width:260px;text-align:center}
  .feature .ring{width:196px;height:196px;border:3px solid var(--ink);border-radius:50%;margin:0 auto;display:flex;align-items:center;justify-content:center}
  .feature .ring .photo{position:static;width:172px;height:172px;border-radius:50%}
  .feature h3{margin-top:18px;font-size:22px;font-weight:600;color:var(--navy);letter-spacing:1px}
  .feature p{margin-top:8px;font-size:11px;line-height:1.5;color:var(--text)}

  /* process */
  .process .step{position:absolute;width:220px}
  .process .step .item-title{font-size:18px}
  .process .step .item-copy{margin-top:4px}

  /* list */
  .listing .body-copy{position:absolute;left:60px;top:110px;width:820px;font-size:15px}
  .listing .entry{position:absolute;left:60px;display:flex;gap:22px;align-items:flex-start}
  .listing .badge{width:36px;height:36px;border-radius:50%;background:var(--gold);color:var(--ink);font-size:11px;font-weight:700;display:flex;align-items:center;justify-content:center;margin-top:18px}
  .listing .entry .item-title{font-size:22px;color:var(--ink)}
  .listing .entry .item-copy{font-size:14px;color:var(--text);width:600px}
</style>
</head>
<body>
<main class="deck">

  <!-- Cover -->
  <div class="frame"><section class="slide cover">
    <div class="photo" role="img" aria-label="Aerial photo of a city skyline with high-rise towers"></div>
    <div class="top-block"></div>
    <div class="logo-box"><span>logo</span></div>
    <div class="accent"></div>
    <h1 class="title"><span class="big">LOREN</span><span class="small">IPSUM</span></h1>
  </section></div>

  <!-- Grid of topics -->
  <div class="frame"><section class="slide">
    <div class="slide-header"><span class="bar"></span><h2>LOREN IPSUM</h2></div>
    <div class="header-rule" style="left:300px;width:610px"></div>
    <div class="grid">
      <div class="cell gold">
        <svg width="90" height="90" viewBox="0 0 90 90" fill="none" stroke="var(--deep-blue)" stroke-width="4"><circle cx="42" cy="48" r="30"/><circle cx="42" cy="48" r="18"/><circle cx="42" cy="48" r="6"/><path d="M42 48 L72 18 M64 16 L72 18 L74 26"/></svg>
      </div>
      <div class="cell plain"><div class="item-title">02 Title Here</div><div class="item-copy">Lorem ipsum dolor sit amet, consectetuer adipiscing elit, sed diam nonummy nibh euismod tincidunt ut.</div></div>
      <div class="cell gold">
        <svg width="90" height="90" viewBox="0 0 90 90" fill="none" stroke="var(--deep-blue)" stroke-width="4"><circle cx="30" cy="30" r="10"/><circle cx="60" cy="30" r="10"/><path d="M12 70 Q12 48 30 48 Q42 48 45 56 Q48 48 60 48 Q78 48 78 70"/></svg>
      </div>
      <div class="cell plain"><div class="item-title">04 Title Here</div><div class="item-copy">Lorem ipsum dolor sit amet, consectetuer adipiscing elit, sed diam nonummy nibh euismod tincidunt ut.</div></div>
      <div class="cell plain"><div class="item-title">01 Title Here</div><div class="item-copy">Lorem ipsum dolor sit amet, consectetuer adipiscing elit, sed diam nonummy nibh euismod tincidunt ut.</div></div>
      <div class="cell gold">
        <svg width="90" height="90" viewBox="0 0 90 90" fill="none" stroke="var(--deep-blue)" stroke-width="4"><path d="M10 80 H82"/><rect x="16" y="56" width="10" height="24"/><rect x="34" y="46" width="10" height="34"/><rect x="52" y="38" width="10" height="42"/><rect x="70" y="28" width="10" height="52"/><path d="M14 46 L36 30 L54 34 L78 12"/><circle cx="46" cy="14" r="8"/></svg>
      </div>
      <div class="cell plain"><div class="item-title">03 Title Here</div><div class="item-copy">Lorem ipsum dolor sit amet, consectetuer adipiscing elit, sed diam nonummy nibh euismod tincidunt ut.</div></div>
      <div class="cell gold">
        <svg width="90" height="90" viewBox="0 0 90 90" fill="none" stroke="var(--deep-blue)" stroke-width="4"><circle cx="26" cy="36" r="9"/><circle cx="64" cy="36" r="9"/><path d="M10 72 Q10 52 26 52 Q40 52 40 72 M50 72 Q50 52 64 52 Q80 52 80 72"/><rect x="34" y="8" width="26" height="16" rx="3"/></svg>
      </div>
    </div>
    <div class="footer-band"><span class="logo-mark">logo</span><span class="page-no">04</span></div>
  </section></div>

  <!-- Intro text with photo -->
  <div class="frame"><section class="slide intro">
    <svg class="dark-panel" width="960" height="540" viewBox="0 0 960 540">
      <polygon points="600,0 960,0 960,484 820,484" fill="var(--ink)"/>
      <polygon points="600,160 860,120 880,300 740,420 560,340" fill="url(#sky)" role="img" aria-label="City skyline photo in an angular frame"/>
      <polyline points="840,150 872,146 886,290 866,308" fill="none" stroke="var(--gold)" stroke-width="8"/>
      <polyline points="600,210 550,350 700,400" fill="none" stroke="var(--gold)" stroke-width="8"/>
      <defs><linearGradient id="sky" x1="0" y1="0" x2="0" y2="1"><stop offset="0" stop-color="#d3dce6"/><stop offset=".5" stop-color="#8c9db0"/><stop offset="1" stop-color="#4b5a6b"/></linearGradient></defs>
    </svg>
    <div class="slide-header"><span class="bar"></span><h2>LOREN IPSUM</h2></div>
    <div class="header-rule" style="left:300px;width:260px"></div>
    <p class="body-copy">Lorem ipsum dolor sit amet, consectetuer adipiscing elit, sed diam nonummy nibh euismod tincidunt ut laoreet dolore magna aliquam erat volutpat.</p>
    <div class="icon-row" style="top:230px">
      <svg width="54" height="54" viewBox="0 0 54 54" fill="none" stroke="var(--deep-blue)" stroke-width="3"><circle cx="25" cy="29" r="20"/><circle cx="25" cy="29" r="12"/><circle cx="25" cy="29" r="4"/><path d="M25 29 L46 8 M40 7 L46 8 L47 14"/></svg>
      <span class="divider"></span>
      <p>Lorem ipsum dolor sit amet, consectetuer adipiscing elit, sed diam nonummy nibh euismod tincidunt ut laoreet dolore magna aliquam.</p>
    </div>
    <div class="icon-row" style="top:320px">
      <svg width="54" height="54" viewBox="0 0 54 54" fill="none" stroke="var(--deep-blue)" stroke-width="3"><path d="M4 48 H50 M10 48 V34 H22 V48 M22 48 V24 H34 V48 M34 48 V38 H46 V48 M28 24 V6 L40 10 L28 14"/></svg>
      <span class="divider"></span>
      <p>Lorem ipsum dolor sit amet, consectetuer adipiscing elit, sed diam nonummy nibh euismod tincidunt ut laoreet dolore magna aliquam.</p>
    </div>
    <div class="footer-band"><span class="logo-mark">logo</span><span class="page-no">02</span></div>
  </section></div>

  <!-- Process curve -->
  <div class="frame"><section class="slide process">
    <div class="slide-header"><span class="bar"></span><h2>LOREN IPSUM</h2></div>
    <div class="header-rule" style="left:300px;width:620px"></div>
    <svg style="position:absolute;left:0;top:0" width="960" height="540" viewBox="0 0 960 540" fill="none">
      <path d="M470 130 V230" stroke="var(--grey-1)" stroke-width="72"/>
      <path d="M470 230 A90 90 0 0 0 560 320" stroke="var(--grey-2)" stroke-width="72"/>
      <path d="M560 320 A90 90 0 0 0 650 230" stroke="var(--grey-3)" stroke-width="72"/>
      <path d="M650 231 V190" stroke="var(--grey-4)" stroke-width="72"/>
      <path d="M650 192 C650 120 700 100 770 100" stroke="var(--deep-blue)" stroke-width="72"/>
      <polygon points="760,50 850,80 790,150" fill="var(--gold)"/>
      <g stroke="#fff" stroke-width="2.5">
        <circle cx="470" cy="170" r="13"/><circle cx="470" cy="170" r="5"/>
        <path d="M505 290 l12 -8 l12 8 M511 296 h16"/>
        <path d="M590 290 v-14 M600 290 v-20 M610 290 v-26 M586 272 l12 -10 l14 -8"/>
        <circle cx="650" cy="215" r="10"/><circle cx="650" cy="215" r="3"/>
      </g>
      <g stroke="var(--grey-1)" stroke-width="1.5">
        <path d="M300 190 H400 L420 210 H434"/>
        <path d="M380 310 H440 L460 290 H480"/>
        <path d="M560 356 V392"/>
        <path d="M686 200 H730 V180 H770"/>
      </g>
    </svg>
    <div class="step" style="left:80px;top:150px"><div class="item-title">01 Title Here</div><div class="item-copy">Lorem ipsum dolor sit amet, consectetuer adipiscing elit, sed diam nonummy</div></div>
    <div class="step" style="left:160px;top:290px"><div class="item-title">02 Title Here</div><div class="item-copy">Lorem ipsum dolor sit amet, consectetuer adipiscing elit, sed diam nonummy</div></div>
    <div class="step" style="left:490px;top:400px;width:300px"><div class="item-title">03 Title Here</div><div class="item-copy">Lorem ipsum dolor sit amet, consectetuer adipiscing elit, sed diam.</div></div>
    <div class="step" style="left:790px;top:170px;width:160px"><div class="item-title">04 Title Here</div><div class="item-copy">Lorem ipsum dolor sit amet, consectetuer, sed diam.</div></div>
    <div class="footer-band"><span class="logo-mark">logo</span><span class="page-no">05</span></div>
  </section></div>

  <!-- Three features -->
  <div class="frame"><section class="slide">
    <div class="slide-header"><span class="bar"></span><h2>LOREN IPSUM</h2></div>
    <div class="header-rule" style="left:300px;width:610px"></div>
    <article class="feature" style="left:50px">
      <div class="ring"><div class="photo hall-photo" role="img" aria-label="Interior of a large warehouse hall"></div></div>
      <h3>LOREN IPSUM</h3>
      <p>Lorem Ipsum is simply dummy text of the printing and typesetting industry. Lorem Ipsum has been the industry's standard dummy text ever since the 1500s.</p>
    </article>
    <article class="feature" style="left:350px">
      <div class="ring"><div class="photo hall-photo" role="img" aria-label="Interior of a large warehouse hall"></div></div>
      <h3>LOREN IPSUM</h3>
      <p>Lorem Ipsum is simply dummy text of the printing and typesetting industry. Lorem Ipsum has been the industry's standard dummy text ever since the 1500s.</p>
    </article>
    <article class="feature" style="left:650px">
      <div class="ring"><div class="photo hall-photo" role="img" aria-label="Interior of a large warehouse hall"></div></div>
      <h3>LOREN IPSUM</h3>
      <p>Lorem Ipsum is simply dummy text of the printing and typesetting industry. Lorem Ipsum has been the industry's standard dummy text ever since the 1500s.</p>
    </article>
    <div class="footer-band"><span class="logo-mark">logo</span><span class="page-no">03</span></div>
  </section></div>

  <!-- Text with numbered points -->
  <div class="frame"><section class="slide listing">
    <div class="slide-header"><span class="bar"></span><h2>LOREN IPSUM</h2></div>
    <div class="header-rule" style="left:300px;width:620px"></div>
    <p class="body-copy">It is a long established fact that a reader will be distracted by the readable content of a page when looking at its layout. It is a long established fact that a reader will be distracted by the readable content of a page when looking at its layout.</p>
    <div class="entry" style="top:250px">
      <span class="badge">01</span>
      <div><div class="item-title">Simple Text One</div><div class="item-copy">Lorem Ipsum is simply dummy text of the printing and typesetting industry.</div></div>
    </div>
    <div class="entry" style="top:340px">
      <span class="badge">02</span>
      <div><div class="item-title">Simple Text Two</div><div class="item-copy">Lorem Ipsum is simply dummy text of the printing and typesetting industry.</div></div>
    </div>
    <div class="footer-band"><span class="logo-mark">logo</span><span class="page-no">06</span></div>
  </section></div>

</main>
</body>
</html>
```